Brisk Bookings needs a New Home page

We provide online appointment scheduling. There are many schedulers out there. Ours is unique because the scheduler is shown in one compact view that can be easily incorporated into the customer's website or Chatterloop page. Whether our customer is a solo hair-stylist or a large testing center with hundreds of testing seats at multiple locations, our customer still gets the same easy-to-use, one-page scheduling experience.

Our current home page, briskbookings.com, feels cluttered and outdated. We want something more modern and minimal.

Here are web pages we like:
plumtrellis.com
fernquay.com
gossamo.io

We are not unhappy with the current logo or color scheme.

Need very clear call(s) to action (i.e. sign up for trial, schedule a demo).
Design needs to look good on devices of varying size.

Here are some ideas:
“Simple Online Scheduling” - Simple, compact design, easy-to-use & powerful, time-saving, chaos-taming, affordable, one page scheduling
“Stay in touch” - Basic email confirmations, reminders or targeted email notifications for follow-ups, no shows and more
“Multiple locations? No problem” - Schedule for multiple locations on one scheduler -
“Resource Pools” - Batting cages, clerks at the BQT, computers in a lab, pilates reformer machines
“Go Social” - Scheduling for Chatterloop and mobile devices
“Visual Reporting” - Reports
“Trusted” - Testimonials, reliable since 2005, etc.
List of industries (with links to industry-specific pages)

Ultimately want to redevelop the full site.

Reason: Please do not submit any new designs. We are now just wrapping up polling and discussing details. Thank you to all designers who have submitted. We feel lucky to get to chose from many great designs.

Target Market(s)

Audience is very broad including solo entrepreneurs (massage therapist, accountants, lawyers), educational institutions (elementary schools, university departments, advisers, testing centers), health care providers and screening services, to government.

Industry/Entity Type

Online

Requirements
Must have
• Call(s) to action, i.e. sign up for trial, schedule a demo.
• Look good on devices of different sizes.

```html
<!DOCTYPE html>
<html lang="en">
<head>
<meta charset="utf-8">
<title>Brisk Bookings – Home</title>
<link rel="stylesheet" href="https://fonts.googleapis.com/css2?family=Arimo:wght@400;700&family=Ubuntu:wght@400;500&display=swap">
<style>
:root{
  --blue:#1a8fd6;
  --blue-dark:#0f7cc0;
  --step-blue:#2ca6f0;
  --ink:#222;
  --text:#444;
  --muted:#777;
  --light:#eeeeef;
  --line:#d8d8d8;
  --yellow:#efc818;
  --yellow-edge:#c9702a;
  --green:#1fe060;
  --green-edge:#c9a32a;
  --footer:#1e1e1e;
  --footer-text:#5c5c5c;
  --teal-a:#3d7f96;
  --teal-b:#6ea9b4;
  --white:#fff;
}
*{box-sizing:border-box;margin:0;padding:0}
html,body{width:1200px;height:2247px;overflow:hidden}
body{position:relative;background:var(--white);font-family:"Arimo",Arial,sans-serif;color:var(--text)}
.abs{position:absolute}

/* top utility bar */
.utility-bar{left:0;top:0;width:1200px;height:33px;border-bottom:1px solid var(--line);background:#fafafa}
.crumbs{left:200px;top:11px;font-size:12px;color:var(--ink)}
.crumbs span{margin:0 4px;color:var(--muted)}
.social-top{left:764px;top:9px;display:flex;gap:14px}
.social-top i{display:block;width:15px;height:15px;border-radius:50%;background:#c4c4c4}
.search-tab{left:945px;top:0;width:36px;height:33px;border-left:1px solid var(--line);border-right:1px solid var(--line);background:var(--white)}

/* header */
.site-header{left:0;top:33px;width:1200px;height:99px;background:var(--white);border-bottom:4px solid var(--blue)}
.brand{left:200px;top:96px;display:flex;align-items:center;gap:10px;font-size:23px;color:var(--ink)}
.brand i{display:block;width:22px;height:22px;border-radius:50%;background:var(--blue)}
.main-nav{left:578px;top:33px;display:flex;height:95px}
.main-nav a{display:flex;align-items:center;padding:0 16px;font-size:12px;color:var(--ink);text-decoration:none}
.main-nav a.active{background:var(--blue);color:var(--white);padding:0 12px}

/* hero slider */
.hero{left:0;top:132px;width:1200px;height:370px;background:linear-gradient(90deg,#2c2e31,#5e6063 32%,#4a4c4f 55%,#38393c 80%,#232426)}
.hero-devices{left:210px;top:160px;width:260px;height:326px;border-radius:8px;background:linear-gradient(160deg,#2a2a2e,#5b5e66 60%,#c9ccd2)}
.hero-title{left:638px;top:186px;font-size:25px;font-weight:700;color:var(--white)}
.steps{left:640px;top:238px;list-style:none}
.steps li{display:flex;align-items:center;gap:24px;height:35px;font-size:18px;color:var(--step-blue)}
.steps li.faded{color:var(--blue)}
.steps .box{display:block;width:16px;height:16px;background:var(--white);flex:none}
.slide-arrow{top:283px}
.dots{left:570px;top:470px;display:flex;gap:6px}
.dots i{display:block;width:10px;height:10px;border-radius:50%;background:var(--white)}
.dots i.on{background:var(--blue);box-shadow:0 0 0 2px var(--white)}

/* welcome */
.welcome{left:0;top:502px;width:1200px;height:158px;background:var(--light)}
.section-title{width:1200px;left:0;text-align:center;font-size:29px;font-weight:400;color:var(--blue)}
.lede{left:210px;width:780px;text-align:center;font-size:10px;line-height:15px;color:var(--text)}

/* how it works */
.demo-video{left:398px;top:800px;width:406px;height:228px;border-radius:10px 10px 4px 4px;background:linear-gradient(180deg,#1d1d20 0,#e9edf3 14%,#f4f6f9 80%,#c6c8cb)}
.play{left:585px;top:878px;width:32px;height:32px}
.cta{top:1057px;width:233px;height:60px;display:flex;align-items:center;justify-content:center;font-size:20px;color:var(--ink);text-decoration:none}
.cta-demo{left:340px;background:var(--yellow);border-bottom:4px solid var(--yellow-edge)}
.cta-trial{left:615px;background:var(--green);border-bottom:4px solid var(--green-edge)}

/* scheduler panel */
.panel{top:1180px;height:362px;background:#f0f0f0;border:1px solid #e2e2e2}
.scheduler{left:200px;width:420px;padding:0 18px}
.panel-title{font-size:20px;font-weight:400;color:var(--blue);margin-top:21px}
.scheduler p.intro{font-size:10px;line-height:15px;margin-top:28px;color:var(--text)}
.features{display:flex;justify-content:space-between;margin-top:26px}
.feature{width:125px;text-align:center}
.feature .tile{width:68px;height:60px;margin:0 auto;background:var(--blue);display:flex;align-items:center;justify-content:center}
.feature h3{font-size:15px;font-weight:400;color:var(--blue);margin-top:7px}
.feature p{height:36px;font-size:10px;line-height:12px;color:var(--ink);margin-top:3px}
.feature a{display:block;font-size:10px;color:var(--blue);margin-top:8px;text-decoration:none}

.booking{left:683px;width:319px;padding:0 17px}
.booking .panel-title{text-align:center;margin-top:13px;font-size:19px}
.field{height:34px;margin-top:11px;background:var(--white);border:1px solid #cfcfcf;font-size:10px;padding:11px 16px;color:var(--muted)}
.field:first-of-type{margin-top:12px}
.field.area{height:75px}
.submit{float:right;margin-top:13px;width:100px;height:38px;background:var(--blue);color:var(--white);font-weight:700;font-size:15px;display:flex;align-items:center;justify-content:center}

/* news */
.tabs{left:201px;top:1570px;display:flex}
.tab{width:122px;height:46px;display:flex;align-items:center;justify-content:center;font-size:15px;color:var(--ink);border:1px solid #ddd;border-bottom:none;background:var(--white)}
.tab.off{width:108px;height:42px;margin-top:4px;background:linear-gradient(#fafafa,#ddd)}
.news{left:201px;top:1615px;width:456px;height:242px;border:1px solid #ddd;padding:0 18px;font-family:"Ubuntu",sans-serif}
.post{position:relative;height:112px;border-bottom:1px solid #ececec;padding-top:14px;overflow:hidden}
.post:last-child{border:none}
.thumb{float:left;width:96px;height:62px;margin:1px 34px 4px 2px}
.post h4{font-size:12px;font-weight:500;color:var(--ink);padding-right:24px}
.post time{display:block;font-size:9px;color:#aaa;margin-top:3px}
.post .count{position:absolute;right:0;top:14px;font-size:10px;color:#999}
.post p{font-size:11px;line-height:15px;color:#666;margin-top:3px}
.post p b{color:#d8463a;font-weight:400}

.schedule{left:700px;top:1580px;width:260px}
.schedule h2{font-size:20px;font-weight:400;color:var(--blue)}
.schedule .sub{font-size:10px;color:var(--text);margin-top:8px}
.schedule dt{font-size:11px;font-weight:700;color:var(--blue);margin-top:13px}
.schedule dd{font-size:9px;line-height:12px;color:#666;margin-top:3px}

/* stats band */
.stats{left:0;top:1882px;width:1200px;height:131px;background:linear-gradient(90deg,var(--teal-a),var(--teal-b) 50%,var(--teal-a))}
.stats-figure{left:211px;top:1920px;font-size:24px;line-height:31px;color:var(--white)}
.stats-copy{left:469px;top:1920px;width:240px;font-size:13px;line-height:15px;color:var(--white)}
.partner-badge{left:716px;top:1902px;width:225px;height:88px;background:var(--white)}

/* footer */
.site-footer{left:0;top:2013px;width:1200px;height:213px;background:var(--footer)}
.fcol{top:2050px}
.fcol h5{font-size:11px;color:var(--white);font-weight:700}
.fcol p{font-size:9px;line-height:12px;color:var(--footer-text);margin-top:26px;width:160px}
.fcol ul{list-style:none;margin-top:19px;width:175px}
.fcol li{font-size:9px;color:var(--footer-text);height:28px;border-bottom:1px solid #2d2d2d;padding-top:4px}
.follow{display:flex;gap:3px;margin-top:14px}
.follow i{display:block;width:18px;height:18px;background:#777}
.bottom-bar{left:0;top:2226px;width:1200px;height:21px;background:var(--blue-dark);color:var(--white);font-size:11px;text-align:center;line-height:21px}
</style>
</head>
<body>

<div class="abs utility-bar"></div>
<nav class="abs crumbs">Home<span>\</span>About Us<span>\</span>Contact Us</nav>
<div class="abs social-top" aria-label="Social links"><i></i><i></i><i></i><i></i><i></i><i></i></div>
<div class="abs search-tab">
  <svg width="36" height="33" viewBox="0 0 36 33"><circle cx="16" cy="14" r="5" fill="none" stroke="#d8463a" stroke-width="2"/><line x1="20" y1="18" x2="24" y2="22" stroke="#d8463a" stroke-width="2"/></svg>
</div>

<header class="abs site-header"></header>
<div class="abs brand"><i></i>Brisk Bookings</div>
<nav class="abs main-nav">
  <a class="active" href="#">See it Work</a>
  <a href="#">Who it's For</a>
  <a href="#">Our Scheduler</a>
  <a href="#">Free Trial</a>
  <a href="#">Dig In</a>
</nav>

<section class="abs hero" role="img" aria-label="Blurred office background"></section>
<div class="abs hero-devices" role="img" aria-label="Desktop, tablet and phone showing the scheduler"></div>
<h1 class="abs hero-title">Easy One Page Scheduling</h1>
<ul class="abs steps">
  <li class="faded"><svg class="box" viewBox="0 0 16 16"><rect width="16" height="16" fill="#fff"/><path d="M3 8l4 4 7-9" fill="none" stroke="#1a8fd6" stroke-width="2"/></svg>Select a date</li>
  <li class="faded"><span class="box"></span>Select a service</li>
  <li><span class="box"></span>Select an opening</li>
  <li><span class="box"></span>Select a date</li>
  <li><span class="box"></span>Enter contact information</li>
  <li class="faded"><span class="box"></span>Confirm appointment</li>
</ul>
<svg class="abs slide-arrow" style="left:58px" width="20" height="28" viewBox="0 0 20 28"><path d="M15 3L5 14l10 11" fill="none" stroke="#1a8fd6" stroke-width="5"/></svg>
<svg class="abs slide-arrow" style="left:1104px" width="20" height="28" viewBox="0 0 20 28"><path d="M5 3l10 11L5 25" fill="none" stroke="#1a8fd6" stroke-width="5"/></svg>
<div class="abs dots"><i class="on"></i><i></i><i></i></div>

<section class="abs welcome"></section>
<h2 class="abs section-title" style="top:527px">Welcome Brisk Bookings</h2>
<p class="abs lede" style="top:576px">Lorem ipsum dolor sit amet, consectetur adipiscing elit. Nulla convallis egestas rhoncus. Donec facilisis fermentum sem, ac viverra ante luctus vel. Donec vel mauris quam. Aliquam pellentesque pellentesque turpis, ut bibendum sapien sollicitudin nec. Pellentesque posuere ornare placerat. Suspendisse potenti. Quisque massa tortor, tristique non tristique at, luctus sed massa. Donec libero eros, mollis ac...Lorem ipsum dolor sit amet, consectetur adipiscing elit. Nulla convallis egestas rhoncus. Donec facilisis fermentum sem, ac viverra ante luctus vel. Donec vel mauris quam. Aliquam pellentesque pellentesque turpis, ut bibendum sapien sollicitudin nec</p>

<h2 class="abs section-title" style="top:693px">How It Works</h2>
<p class="abs lede" style="top:742px">Lorem ipsum dolor sit amet, consectetur adipiscing elit. Nulla convallis egestas rhoncus. Donec facilisis fermentum sem, ac viverra ante luctus vel. Donec vel mauris quam. Aliquam pellentesque pellentesque turpis, ut bibendum sapien sollicitudin nec. Pellentesque posuere ornare placerat. Suspendisse potenti. Quisque massa tortor, tristique non tristique at,</p>
<div class="abs demo-video" role="img" aria-label="Laptop playing the product demo video"></div>
<svg class="abs play" viewBox="0 0 32 32"><circle cx="16" cy="16" r="16" fill="#d4402c"/><path d="M12 9l11 7-11 7z" fill="#fff"/></svg>

<a class="abs cta cta-demo" href="#">Request a Demo</a>
<a class="abs cta cta-trial" href="#">Get a Free Trail</a>

<section class="abs panel scheduler">
  <h2 class="panel-title">OUR SCHEDULER</h2>
  <p class="intro">Lorem ipsum dolor sit amet, consectetur adipiscing elit. Nulla convallis egestas rhoncus. Donec facilisis fermentum sem, ac viverra ante luctus vel. Donec vel mauris quam. Aliquam pellentesque pellentesque turpis, ut bibendum sapien sollicitudin nec. Pellentesque posuere ornare placerat. Suspendisse potenti. Quisque massa tortor, tristique non tristique at,</p>
  <div class="features">
    <div class="feature">
      <div class="tile"><svg width="36" height="36" viewBox="0 0 36 36"><circle cx="18" cy="18" r="14" fill="none" stroke="#fff" stroke-width="3"/><path d="M18 9v9l6 4" fill="none" stroke="#fff" stroke-width="3"/></svg></div>
      <h3>Save time</h3>
      <p>Teach Forward saves "considerable man hours..."</p>
      <a href="#">Read more..</a>
    </div>
    <div class="feature">
      <div class="tile"><svg width="36" height="40" viewBox="0 0 36 40"><circle cx="18" cy="6" r="4" fill="none" stroke="#fff" stroke-width="3"/><line x1="18" y1="10" x2="18" y2="36" stroke="#fff" stroke-width="3"/><line x1="10" y1="16" x2="26" y2="16" stroke="#fff" stroke-width="3"/><path d="M4 24c2 8 8 12 14 12s12-4 14-12" fill="none" stroke="#fff" stroke-width="3"/></svg></div>
      <h3>Simplify</h3>
      <p>Lanai Wellness has "eliminated missed or mixed-up appointments"</p>
      <a href="#">Read more..</a>
    </div>
    <div class="feature">
      <div class="tile"><svg width="36" height="36" viewBox="0 0 36 36"><circle cx="14" cy="14" r="9" fill="none" stroke="#fff" stroke-width="4"/><line x1="21" y1="21" x2="32" y2="32" stroke="#fff" stroke-width="5"/></svg></div>
      <h3>It's affordable!</h3>
      <p>For Stillwater Massage it's "one of the best investments..."</p>
      <a href="#">Read more..</a>
    </div>
  </div>
</section>

<section class="abs panel booking">
  <h2 class="panel-title">Get An Appointment</h2>
  <div class="field">Name</div>
  <div class="field">Mobile</div>
  <div class="field">Email</div>
  <div class="field">Appointment Date</div>
  <div class="field area">Message</div>
  <div class="submit">Submit</div>
</section>

<div class="abs tabs"><div class="tab">News</div><div class="tab off">Blog</div></div>
<section class="abs news">
  <article class="post">
    <div class="thumb" role="img" aria-label="Person outdoors in a red jacket" style="background:linear-gradient(135deg,#8a9a6a,#c0483a 55%,#7d8c5a)"></div>
    <span class="count">2</span>
    <h4>Awesome Slider Post</h4>
    <time>May 30, 2013</time>
    <p>Lorem ipsum dolor sit amet, consectetur adipiscing elit, sed do eiusmod tempor incididunt ut labore et dolore magna aliqua. Ut enim ad minim veniam, quis nostrud exercitation ullamco laboris nisi ut <b>»</b></p>
  </article>
  <article class="post">
    <div class="thumb" role="img" aria-label="Business team in an office" style="background:linear-gradient(135deg,#9fb3c8,#e2d6c8 55%,#5a6f86)"></div>
    <span class="count">0</span>
    <h4>Another Gallery post</h4>
    <time>May 1, 2013</time>
    <p>Integer leo magna, adipiscing a ligula quis, tempor porta ipsum. Nullam quis eros congue, tempus dui eleifend, vehicula leo. Duis tincidunt justo non laoreet condimentum. Sed sit amet arcu blandit <b>»</b></p>
  </article>
</section>

<aside class="abs schedule">
  <h2>Current Schedule</h2>
  <p class="sub">Currently Schedule Online appointment for:</p>
  <dl>
    <dt>Account</dt><dd>Medora is a PressKit premium theme suitable for any medical and health related projects or businesses.</dd>
    <dt>Online</dt><dd>Wether you need to create a site for a medical center, spa, gym, vet shop: This theme is right for you. Check all the features and fall in love with Medora.</dd>
    <dt>Post</dt><dd>Medora is a PressKit premium theme suitable for any medical and health related projects or businesses.</dd>
    <dt>Appointment</dt><dd>Wether you need to create a site for a medical center, spa, gym, vet shop: This theme is right for you. Check all the features and fall in love with Medora.</dd>
  </dl>
</aside>

<section class="abs stats"></section>
<p class="abs stats-figure">2,000,000+ SBOA<br>appointments!</p>
<svg class="abs" style="left:410px;top:1915px" width="30" height="68" viewBox="0 0 30 68"><path d="M4 3c10 0 10 6 10 14s0 14 12 17C14 37 14 44 14 51s0 14-10 14" fill="none" stroke="#f0b030" stroke-width="4"/></svg>
<p class="abs stats-copy">Students schedule time with teachers using Brisk Bookings. We are proud to aid in the vision of SBOA to provide world-class education</p>
<div class="abs partner-badge"></div>

<footer class="abs site-footer"></footer>
<div class="abs fcol" style="left:200px"><h5>About us</h5><p>Lorem ipsum dolor sit amet, consectetur adipiscing elit. Nulla convallis egestas rhoncus. Donec facilisis fermentum sem, ac viverra ante</p></div>
<div class="abs fcol" style="left:420px"><h5>Products</h5><ul><li>Network &amp; Convergence Services</li><li>Infrastructure SecurityServices</li><li>Enterprise Computing Services</li></ul></div>
<div class="abs fcol" style="left:630px"><h5>Industries</h5><ul><li>Architecture</li><li>Financial Services</li><li>Housing Associations</li><li>Non-profit</li><li>Retails</li></ul></div>
<div class="abs fcol" style="left:842px"><h5>Follow us</h5><div class="follow"><i style="background:#3b5a9a"></i><i style="background:#2aa3d8"></i><i style="background:#d04a36"></i><i style="background:#c8232c"></i><i style="background:#eee"></i></div></div>
<div class="abs bottom-bar">Copy right@ Brisk Bookings. 2013</div>

</body>
</html>
```